indépendant en tant que Massothérapeute et Préparateur Mental, j'ai besoin de ...

Massothérapeute et préparateur mental indépendant, je recherche une carte de visite sobre et dynamique, sans images liées au massage ou à la préparation mentale mais intégrant mon logo. Les couleurs que j'aime bien sont : Blanc, gris, anthracite, noir et jaune

Contact Information for Business Card

carte de préférence Horizontale
neutre qui puisse toucher le deux domaines Massothérapie et préparation mentale

Requirements
Must have
• mon projet doit intégrer au recto:
LOGO
Loïc Vermande
078 315 26 49
info@loicvermande-exemple.ch
et éventuellement www.loicvermande-exemple.ch

et au verso les deux adresses:

Chemin des Ormelets 27B
1400 Yverdon-les-Bains

Rue des Tanneries 9
1700 Fribourg

Should not have
• mon projet ne doit pas contenir d'image en liens avec le massage ni la préparation mentale.

```html
<!DOCTYPE html>
<html lang="fr">
<head>
<meta charset="utf-8">
<title>Loïc Vermande – Cartes de visite</title>
<link href="https://fonts.googleapis.com/css2?family=Questrial&display=swap" rel="stylesheet">
<style>
  :root {
    --backdrop: #9b9b9b;
    --band: #666666;
    --paper: #e8e9eb;
    --ink: #5e5e5e;
    --ink-soft: #7a7a7a;
    --on-band: #e8e9eb;
    --rule: #9c9c9c;
  }
  * { box-sizing: border-box; margin: 0; padding: 0; }
  html, body { width: 1200px; height: 900px; overflow: hidden; }
  body {
    background: var(--backdrop);
    font-family: "Questrial", "Helvetica Neue", Arial, sans-serif;
    display: flex; align-items: center; justify-content: center; gap: 50px;
  }
  .card {
    width: 540px; height: 350px; position: relative; overflow: hidden;
    background: var(--paper);
    box-shadow: 0 14px 30px rgba(40, 42, 56, 0.35);
  }
  .band { position: absolute; left: 0; right: 0; top: 0; background: var(--band); }

  /* Front */
  .card--front .band { height: 112px; }
  .brand { position: absolute; display: flex; align-items: center; gap: 12px; }
  .brand__mark { width: 14px; height: 14px; background: currentColor; }
  .brand__text { display: flex; flex-direction: column; }
  .brand__name { font-size: 30px; letter-spacing: 0.5px; line-height: 1; }
  .brand__tagline { font-size: 11px; letter-spacing: 1.2px; text-transform: uppercase; margin-top: 6px; }
  .card--front .brand { left: 40px; top: 28px; color: var(--on-band); }

  .identity { position: absolute; left: 88px; top: 146px; width: 330px; }
  .identity__name {
    font-size: 30px; color: var(--ink); text-transform: uppercase; letter-spacing: 0.5px;
    padding-bottom: 12px; border-bottom: 1px solid var(--rule);
  }
  .contact { list-style: none; margin-top: 16px; padding-left: 22px; }
  .contact li {
    display: flex; align-items: center; gap: 10px;
    font-size: 15px; color: var(--ink); line-height: 1.75;
  }
  .contact svg { width: 11px; height: 11px; fill: var(--ink); flex: none; }

  /* Back */
  .card--back .band { height: 218px; }
  .addresses { position: absolute; left: 118px; top: 54px; list-style: none; }
  .addresses li { display: flex; gap: 12px; color: var(--on-band); font-size: 16px; line-height: 1.25; margin-bottom: 14px; }
  .addresses svg { width: 13px; height: 18px; fill: var(--on-band); flex: none; margin-top: 2px; }
  .card--back .brand { right: 36px; bottom: 40px; color: var(--ink); }
  .card--back .brand__name { font-size: 26px; }
  .card--back .brand__tagline { font-size: 9.5px; }
</style>
</head>
<body>

<section class="card card--front" aria-label="Recto">
  <div class="band"></div>
  <div class="brand">
    <span class="brand__mark"></span>
    <div class="brand__text">
      <span class="brand__name">Loïc Vermande</span>
      <span class="brand__tagline">Massothérapeute / Préparateur Mental</span>
    </div>
  </div>
  <div class="identity">
    <h1 class="identity__name">Loïc Vermande</h1>
    <ul class="contact">
      <li>
        <svg viewBox="0 0 24 24" aria-hidden="true"><path d="M6.6 10.8a15.1 15.1 0 0 0 6.6 6.6l2.2-2.2a1 1 0 0 1 1-.25 11.4 11.4 0 0 0 3.6.57 1 1 0 0 1 1 1V20a1 1 0 0 1-1 1A17 17 0 0 1 3 4a1 1 0 0 1 1-1h3.5a1 1 0 0 1 1 1c0 1.25.2 2.45.57 3.57a1 1 0 0 1-.25 1z"/></svg>
        078 315 26 49
      </li>
      <li>
        <svg viewBox="0 0 24 24" aria-hidden="true"><path d="M2 5h20v14H2zm2 2v.3l8 5.2 8-5.2V7z"/></svg>
        info@loicvermande-exemple.ch
      </li>
      <li>
        <svg viewBox="0 0 24 24" aria-hidden="true"><circle cx="12" cy="12" r="9"/></svg>
        www.loicvermande-exemple.ch
      </li>
    </ul>
  </div>
</section>

<section class="card card--back" aria-label="Verso">
  <div class="band"></div>
  <ul class="addresses">
    <li>
      <svg viewBox="0 0 16 22" aria-hidden="true"><path d="M8 0a8 8 0 0 0-8 8c0 6 8 14 8 14s8-8 8-14a8 8 0 0 0-8-8zm0 11a3 3 0 1 1 0-6 3 3 0 0 1 0 6z"/></svg>
      <span>Chemin des Ormelets 27B<br>1400 Yverdon-les-Bains</span>
    </li>
    <li>
      <svg viewBox="0 0 16 22" aria-hidden="true"><path d="M8 0a8 8 0 0 0-8 8c0 6 8 14 8 14s8-8 8-14a8 8 0 0 0-8-8zm0 11a3 3 0 1 1 0-6 3 3 0 0 1 0 6z"/></svg>
      <span>Rue des Tanneries 9<br>1700 Freiburg</span>
    </li>
  </ul>
  <div class="brand">
    <span class="brand__mark"></span>
    <div class="brand__text">
      <span class="brand__name">Loïc Vermande</span>
      <span class="brand__tagline">Massothérapeute / Préparateur Mental</span>
    </div>
  </div>
</section>

</body>
</html>
```